Hot Offer banner for product listing page

Hi, we need a banner in the dimensions 210x390px which will be shown in the product listing on our online shop. There are 18 products and in between randomly there should be 3 banners with three different information.
first banner: fast delivery
The idea is to show a stove which is very "fast". Maybe you can make an effect like in Voidcruiser Halcyon when they activate the warp drive or something similar. Anyway, the banner should indicate that the delivery is very fast for this product.

second banner: Advantage banner
We would like to have a banner which names all our advantages in our online shop. this is the list of advantages:
- over 200,000 satisfied customers
- Best price guarantee
- thousands of devices in stock
- Top ratings

I attached you some examples, just to give you an idea.

```html
<!DOCTYPE html>
<html lang="en">
<head>
<meta charset="utf-8">
<title>Hot Offer Banners</title>
<link rel="stylesheet" href="https://fonts.googleapis.com/css2?family=Orbitron:wght@900&display=swap">
<style>
  :root {
    --backdrop: #412616;
    --band: #f0fb5a;
    --ink: #0b0b0b;
    --paper: #ffffff;
    --burst-core: #120d04;
    --burst-mid: #5a4a06;
    --burst-glow: #d8e83a;
  }
  html, body {
    margin: 0;
    padding: 0;
    overflow: hidden;
  }
  body {
    width: 1200px;
    height: 878px;
    background: var(--backdrop);
    position: relative;
    font-family: "Orbitron", sans-serif;
  }
  .banner {
    position: absolute;
    top: 153px;
    width: 304px;
    height: 566px;
    overflow: hidden;
  }
  .banner--advantages { left: 247px; }
  .banner--delivery { left: 676px; }
  .warp-art {
    position: absolute;
    inset: 0;
    background:
      radial-gradient(ellipse at 50% 48%, var(--burst-core) 0%, #2a2005 30%, var(--burst-mid) 55%, #2a2407 70%, var(--burst-glow) 100%);
  }
  .banner--delivery .warp-art {
    background:
      radial-gradient(ellipse 60% 8% at 60% 48%, rgba(255,255,255,0.55), transparent 70%),
      radial-gradient(ellipse at 50% 48%, var(--burst-core) 0%, #2a2005 30%, var(--burst-mid) 55%, #2a2407 70%, var(--burst-glow) 100%);
  }
  .band {
    position: absolute;
    left: 0;
    right: 0;
    background: var(--band);
    display: flex;
    flex-direction: column;
    align-items: center;
    justify-content: center;
  }
  .slogan {
    margin: 0;
    color: var(--ink);
    font-weight: 900;
    text-transform: uppercase;
    text-align: center;
    transform: skewX(-14deg);
    line-height: 1.08;
    text-shadow:
      1.5px 0 0 var(--paper), -1.5px 0 0 var(--paper),
      0 1.5px 0 var(--paper), 0 -1.5px 0 var(--paper),
      1px 1px 0 var(--paper), -1px -1px 0 var(--paper),
      1px -1px 0 var(--paper), -1px 1px 0 var(--paper);
  }
  .banner-title {
    position: absolute;
    left: 0;
    right: 0;
    top: 238px;
    margin: 0;
    text-align: center;
    color: var(--paper);
    font-weight: 900;
    font-size: 24px;
    letter-spacing: -0.5px;
    transform: skewX(-14deg);
    text-shadow:
      2px 0 0 var(--ink), -2px 0 0 var(--ink),
      0 2px 0 var(--ink), 0 -2px 0 var(--ink),
      2px 2px 0 var(--ink), -2px -2px 0 var(--ink),
      2px -2px 0 var(--ink), -2px 2px 0 var(--ink);
  }
  .banner--advantages .banner-title { top: 85px; }
  .advantage { font-size: 19px; letter-spacing: -0.5px; }
  .band--customers { top: 141px; height: 85px; }
  .band--price { top: 241px; height: 57px; }
  .band--ratings { top: 326px; height: 35px; }
  .band--stock { top: 378px; height: 85px; }
  .band--delivery { top: 226px; height: 93px; }
  .delivery-headline { font-size: 31px; line-height: 1.1; }
</style>
</head>
<body>
  <section class="banner banner--advantages">
    <div class="warp-art" role="img" aria-label="Yellow warp-speed light streaks bursting from a dark centre"></div>
    <h2 class="banner-title">ADVANTAGES</h2>
    <div class="band band--customers"><p class="slogan advantage">Over 200,000<br>satisfied<br>customers</p></div>
    <div class="band band--price"><p class="slogan advantage">Best price<br>guarantee</p></div>
    <div class="band band--ratings"><p class="slogan advantage">Top ratings</p></div>
    <div class="band band--stock"><p class="slogan advantage">Thousands<br>of devices<br>in stock</p></div>
  </section>

  <section class="banner banner--delivery">
    <div class="warp-art" role="img" aria-label="Stove rushing through yellow warp-speed light streaks with white motion trails"></div>
    <div class="band band--delivery"><p class="slogan delivery-headline">Fast<br>delivery</p></div>
  </section>
</body>
</html>
```